brelvatrim.com

I have a site already disigned, however at the time I had no clue of how and what my site should look like. Still pretty cluless but I know I need to make some fundamenlal changes. I'm looking fora designer who understands how to connect with the cosumer with a ballance of visual and content with SEO in mind.I have a lot of content ready to be added to the mix, just missing alot of bottons for the content for example I have FAQ content but no FAQ botton. There are a lot of things I would like to add and take away from the current site. Here is a list of what I would like to add and subtracted from the site.Take away the find botton and ad contact us change the about botton to about brelvatrim,under that botton i want bottons that lead to News/Events,carreer opertunities,contact us and priacy policy. I also want to add Services offered: personal training,Motivational speeking ,bootcamp conditioning,rondalo,kickboxing cardio,and hip hop cordio. I want to add a botton for testimonials:video and written. I need to add a blog botton, a FAQ botton, and before and after. I want to add a social media botton: pagewall, snapreel,chirpline,pinlocal,clipstream,and spot hopper. I need to add a store botton; T shirts. I would like the contact info the be linked to my email. and I would like would like at the top of contact form to read Request a free info session Now!!! But I don't need a new design I need to add these thing to the one I already have whitch is CMS based

Reason: I need my site to have new logo, just figured out how to down load logo

Reason: I need site to be CMS based so I can up load content and pics

Target Market(s)

People who want to loose weight, mostley women over the age of 30 and men over the age of 40 that income is at least 60,000 a year

Industry/Entity Type

Store

Font styles to use
Sans Serif
Decorative

Colors
000000
ec1f27
0255a3

Requirements
Must have
• Adding the drop downs listed above

```html
<!DOCTYPE html>
<html lang="en">
<head>
<meta charset="utf-8">
<title>Brelvatrim Fitness</title>
<link rel="stylesheet" href="https://fonts.googleapis.com/css2?family=Roboto+Condensed:ital,wght@0,400;0,700;1,400&display=swap">
<style>
:root{
  --red:#cf2b2f;
  --dark:#232323;
  --panel:#2a2a2a;
  --field:#1c1c1c;
  --white:#ffffff;
  --ink:#2b2b2b;
  --photo-light:#bdbdbd;
  --photo-dark:#3a3a3a;
}
*{box-sizing:border-box;margin:0;padding:0}
html,body{width:1200px;height:810px;overflow:hidden}
body{font-family:"Roboto Condensed",Arial,sans-serif;background:var(--white);position:relative}
.hero-photo{position:absolute;left:0;top:0;width:1200px;height:765px;
  background:radial-gradient(ellipse at 70% 40%,#8a8a8a 0%,transparent 55%),linear-gradient(180deg,#d8d8d8 0%,#a9a9a9 35%,#6a6a6a 70%,#4a4a4a 100%)}
.brand{position:absolute;left:193px;top:15px;width:112px;height:112px;border-radius:50%;background:var(--dark);
  display:flex;align-items:center;justify-content:center;color:var(--red);font-weight:700;font-size:17px;letter-spacing:.5px}
.main-nav{position:absolute;left:420px;top:18px;width:400px;display:grid;grid-template-columns:134px 134px 126px;row-gap:6px;text-align:center;color:var(--ink);font-size:14px}
.main-nav span{line-height:18px;white-space:nowrap}
.main-nav .current{position:relative}
.main-nav .current::after{content:"";position:absolute;left:38px;right:38px;bottom:-3px;height:1px;background:var(--red)}
.follow-badge{position:absolute;left:892px;top:15px;width:111px;height:111px;border-radius:50%;overflow:hidden;background:var(--dark);color:var(--white);text-align:center}
.follow-badge .cap{background:var(--red);height:36px;padding-top:16px;font-size:10px}
.follow-badge .nets{display:grid;grid-template-columns:1fr 1fr;gap:3px 4px;padding:10px 14px 0;font-size:8px;line-height:10px}
.tag{position:absolute;color:var(--white);font-size:28px;line-height:43px;padding:0 16px}
.tag-top{left:225px;top:169px;width:310px;background:var(--red)}
.tag-bottom{left:318px;top:212px;width:375px;background:var(--dark);padding-left:34px}
.service{position:absolute;top:374px}
.service .disc{position:absolute;top:0;width:108px;height:108px;border-radius:50%;background:var(--red);display:flex;align-items:center;justify-content:center}
.service .label{position:absolute;top:104px;height:48px;background:var(--dark);color:var(--white);font-size:14px;line-height:15px;padding:10px 0 0 9px}
.service .label svg{position:absolute;right:9px;top:14px}
.panel{position:absolute;top:558px;height:179px;background:var(--panel)}
.panel-head{height:32px;background:var(--red);color:var(--white);font-size:16px;line-height:32px;padding-left:16px;position:relative}
.panel-head svg{position:absolute;right:8px;top:8px}
.blog{left:195px;width:294px}
.post{position:absolute;left:18px;display:flex;gap:12px}
.post .thumb{width:40px;height:38px;background:linear-gradient(135deg,#7d7d7d,#c7c7c7);flex:none}
.post h3{font-size:10px;font-weight:400;color:var(--red);line-height:12px}
.post p{font-size:9.5px;font-style:italic;color:var(--white);line-height:11.5px;width:210px}
.results{left:493px;width:262px}
.results .panel-head{padding-left:9px}
.results .panel-head span+span{position:absolute;left:139px}
.shot{position:absolute;top:39px;width:113px;height:133px;background:var(--white);padding:0}
.shot div{width:100%;height:100%;background:linear-gradient(180deg,#f2f2f2 0%,#d9b59b 45%,#8fc4d8 75%,#f2f2f2 100%)}
.request{left:759px;width:262px}
.request .panel-head{padding-left:11px}
.field{position:absolute;background:var(--field);color:#e6e6e6;font-size:10px;line-height:22px;padding-left:11px}
.field svg{position:absolute;right:8px;top:8px}
.book{position:absolute;left:143px;top:158px;width:100px;height:25px;background:var(--red);color:var(--white);font-size:15px;line-height:25px;text-align:center}
.site-foot{position:absolute;left:0;top:765px;width:1200px;height:45px;background:var(--white);color:var(--ink);font-size:11px}
.site-foot .legal{position:absolute;left:200px;top:15px}
.site-foot .follow{position:absolute;left:803px;top:15px;font-size:10px}
.site-foot .nets{position:absolute;left:880px;top:15px;color:var(--red);font-size:9px;font-weight:700;display:flex;gap:6px}
</style>
</head>
<body>
<div class="hero-photo" role="img" aria-label="Black and white photo of a man doing a plank exercise on a gym bench by large windows"></div>

<div class="brand">BRELVATRIM</div>

<nav class="main-nav">
  <span class="current">HOME</span><span>NEWS/EVENTS</span><span>BLOG</span>
  <span>ABOUT BRELVATRIM</span><span>CARREER OPERTUNITIES</span><span>FAQ's</span>
  <span>GALLERY</span><span>TRAINING</span><span>CONTACT US</span>
</nav>

<div class="follow-badge">
  <div class="cap">FOLLOW US</div>
  <div class="nets"><span>snapreel</span><span>pagewall</span><span>chirpline</span><span>pinlocal</span><span>clipstream</span><span>spot hopper</span></div>
</div>

<div class="tag tag-top">CHANGING LIFESTYLES</div>
<div class="tag tag-bottom">ONE HEART RATE AT A TIME</div>

<div class="service" style="left:209px">
  <div class="disc"><svg width="44" height="44" viewBox="0 0 44 44" fill="#fff"><circle cx="18" cy="8" r="5"/><rect x="12" y="15" width="12" height="16"/><rect x="13" y="31" width="4" height="11"/><rect x="19" y="31" width="4" height="11"/><rect x="24" y="17" width="10" height="3"/><rect x="33" y="13" width="3" height="11"/></svg></div>
  <div class="label" style="width:112px">PERSONAL<br>TRAINING<svg width="12" height="20" viewBox="0 0 12 20"><path d="M2 2l8 8-8 8" stroke="#fff" stroke-width="2.5" fill="none"/></svg></div>
</div>
<div class="service" style="left:347px">
  <div class="disc"><svg width="44" height="50" viewBox="0 0 44 50" fill="#fff"><path d="M12 2h7l5 14h-5zM32 2h-7l-3 9 2 5z"/><circle cx="22" cy="32" r="11"/><circle cx="22" cy="32" r="6" fill="#cf2b2f"/></svg></div>
  <div class="label" style="left:-7px;width:120px">MOTIVATIONAL<br>SPEEKING<svg width="12" height="20" viewBox="0 0 12 20"><path d="M2 2l8 8-8 8" stroke="#fff" stroke-width="2.5" fill="none"/></svg></div>
</div>
<div class="service" style="left:486px">
  <div class="disc"><svg width="62" height="44" viewBox="0 0 62 44" fill="#fff"><circle cx="31" cy="7" r="6"/><rect x="25" y="15" width="12" height="14"/><rect x="25" y="29" width="4" height="13"/><rect x="33" y="29" width="4" height="13"/><rect x="6" y="20" width="50" height="3"/><rect x="4" y="14" width="4" height="15"/><rect x="54" y="14" width="4" height="15"/><rect x="9" y="16" width="3" height="11"/><rect x="50" y="16" width="3" height="11"/></svg></div>
  <div class="label" style="left:-9px;width:122px">BOOTCAMP<br>CONDITIONING<svg width="12" height="20" viewBox="0 0 12 20"><path d="M2 2l8 8-8 8" stroke="#fff" stroke-width="2.5" fill="none"/></svg></div>
</div>
<div class="service" style="left:624px">
  <div class="disc"><svg width="40" height="46" viewBox="0 0 40 46" fill="#fff"><circle cx="24" cy="6" r="5"/><path d="M18 13h9l-2 14 8 6v11h-4v-9l-8-5-2 6H6v-4h8z"/></svg></div>
  <div class="label" style="left:-6px;width:123px">RONDALO<svg width="12" height="20" viewBox="0 0 12 20"><path d="M2 2l8 8-8 8" stroke="#fff" stroke-width="2.5" fill="none"/></svg></div>
</div>
<div class="service" style="left:763px">
  <div class="disc"><svg width="46" height="50" viewBox="0 0 46 50"><rect x="18" y="2" width="10" height="5" fill="#fff"/><circle cx="23" cy="29" r="17" fill="none" stroke="#fff" stroke-width="5"/><path d="M23 29l8-8" stroke="#fff" stroke-width="4"/><rect x="36" y="8" width="5" height="6" fill="#fff" transform="rotate(45 38 11)"/></svg></div>
  <div class="label" style="left:-7px;width:122px">KICKBOXING<br>CARDIO<svg width="12" height="20" viewBox="0 0 12 20"><path d="M2 2l8 8-8 8" stroke="#fff" stroke-width="2.5" fill="none"/></svg></div>
</div>
<div class="service" style="left:901px">
  <div class="disc"><svg width="52" height="46" viewBox="0 0 52 46"><path d="M26 44L6 24C-2 15 4 2 14 2c6 0 10 4 12 7 2-3 6-7 12-7 10 0 16 13 8 22z" fill="#fff"/><path d="M6 23h12l4-7 5 13 4-9 3 3h12" stroke="#cf2b2f" stroke-width="3" fill="none"/></svg></div>
  <div class="label" style="left:-8px;width:123px">HIP HOP<br>CARDIO<svg width="12" height="20" viewBox="0 0 12 20"><path d="M2 2l8 8-8 8" stroke="#fff" stroke-width="2.5" fill="none"/></svg></div>
</div>

<section class="panel blog">
  <div class="panel-head">BLOG POSTS<svg width="12" height="18" viewBox="0 0 12 18"><path d="M2 2l7 7-7 7" stroke="#fff" stroke-width="2.5" fill="none"/></svg></div>
  <div class="post" style="top:46px">
    <div class="thumb" role="img" aria-label="Small photo of people training in a gym"></div>
    <div><h3>Amet, consectetuer adipiscing elit</h3><p>Lorem ipsum dolor sit amet, consectatuer adipiscing elit, sed diam nonummy nibh euismod tincidunt ut laoreet dolore magna.</p></div>
  </div>
  <div class="post" style="top:106px">
    <div class="thumb" role="img" aria-label="Small photo of a woman exercising"></div>
    <div><h3>Amet, consectetuer adipiscing elit</h3><p>Lorem ipsum dolor sit amet, consectatuer adipiscing elrat volutpat. Ut wisi enim ad minim veniam, quis nostrud exerci tation.</p></div>
  </div>
</section>

<section class="panel results">
  <div class="panel-head"><span>BEFORE</span><span>AFTER</span></div>
  <div class="shot" style="left:16px"><div role="img" aria-label="Before photo of a woman in a swimsuit"></div></div>
  <div class="shot" style="left:137px"><div role="img" aria-label="After photo of the same woman, slimmer, in sportswear"></div></div>
</section>

<section class="panel request">
  <div class="panel-head">REQUEST A FREE INFO SESSION NOW</div>
  <div class="field" style="left:17px;top:43px;width:227px">CHOOSE PROGRAM<svg width="8" height="6" viewBox="0 0 8 6"><path d="M1 1l3 3 3-3" stroke="#ccc" fill="none"/></svg></div>
  <div class="field" style="left:17px;top:69px;width:111px">DATE</div>
  <div class="field" style="left:131px;top:69px;width:113px">NUMBER OF PERSONS<svg width="8" height="6" viewBox="0 0 8 6"><path d="M1 1l3 3 3-3" stroke="#ccc" fill="none"/></svg></div>
  <div class="field" style="left:17px;top:94px;width:111px">E-MAIL</div>
  <div class="field" style="left:131px;top:94px;width:113px">PHONE NUMBER</div>
  <div class="field" style="left:17px;top:118px;width:227px;height:34px">MESSAGE</div>
  <div class="book">BOOK NOW</div>
</section>

<footer class="site-foot">
  <span class="legal">BRELVATRIM FITNESS. © 2014. PRIVACY POLICY</span>
  <span class="follow">FOLLOW US</span>
  <span class="nets"><span>snapreel</span><span>pagewall</span><span>chirpline</span><span>pinlocal</span><span>clipstream</span><span>spot hopper</span></span>
</footer>
</body>
</html>
```